Melissa Tarnow Personal Business Card

I like orange. It's would better if my card have an orange background
Address: 4720 Halberd Lane #318
San Jose
California
US
Tel: 4085172946

Industry/Entity Type

Business

```html
<!DOCTYPE html>
<html lang="en">
<head>
<meta charset="utf-8">
<title>Melissa Tarnow — Business Card</title>
<link rel="stylesheet" href="https://fonts.googleapis.com/css2?family=Shadows+Into+Light&family=Arimo:ital@1&display=swap">
<style>
  :root {
    --card-orange: #ff5a00;
    --glow-orange: rgba(255, 150, 90, 0.28);
    --glow-fade: rgba(255, 150, 90, 0);
    --ink-white: #ffffff;
    --ink-outline: rgba(90, 30, 0, 0.55);
  }
  html, body {
    margin: 0;
    padding: 0;
    width: 1200px;
    height: 686px;
    overflow: hidden;
    background: var(--card-orange);
  }
  .card {
    position: relative;
    width: 1200px;
    height: 686px;
    background: var(--card-orange);
    overflow: hidden;
  }
  .card__glow {
    position: absolute;
    left: 100px;
    top: 110px;
    width: 460px;
    height: 400px;
    background: radial-gradient(ellipse 50% 50% at 50% 50%, var(--glow-orange), var(--glow-fade) 75%);
  }
  .card__wisps {
    position: absolute;
    left: 0;
    bottom: 0;
    width: 1200px;
    height: 210px;
    background: linear-gradient(to top, rgba(255, 170, 120, 0.22), rgba(255, 170, 120, 0));
  }
  .card__name {
    position: absolute;
    left: 229px;
    top: 276px;
    margin: 0;
    font-family: "Shadows Into Light", cursive;
    font-weight: 400;
    font-size: 96px;
    line-height: 1;
    letter-spacing: -2px;
    color: var(--ink-white);
    text-shadow:
      1px 1px 0 var(--ink-outline),
      -1px 1px 0 var(--ink-outline),
      1px -1px 0 var(--ink-outline),
      -1px -1px 0 var(--ink-outline);
    white-space: nowrap;
  }
  .card__contact {
    position: absolute;
    left: 714px;
    top: 444px;
    margin: 0;
    font-family: "Arimo", Arial, sans-serif;
    font-style: italic;
    font-size: 23px;
    line-height: 34.5px;
    letter-spacing: 2px;
    word-spacing: 4px;
    color: var(--ink-white);
    white-space: nowrap;
  }
</style>
</head>
<body>
  <main class="card">
    <div class="card__glow" role="img" aria-label="Soft warm light glowing behind the name"></div>
    <div class="card__wisps" role="img" aria-label="Faint light streaks along the bottom edge"></div>
    <h1 class="card__name">Melissa Tarnow</h1>
    <p class="card__contact">
      4720 Halberd Lane #318<br>
      San Jose, California US<br>
      Tel: 4085172946
    </p>
  </main>
</body>
</html>
```